Business Card Design for Marketing Firm

Looking for business card design for higher end marketing firm. Clean but impressionable/trendy. We are a marketing firm that represents manufacturers in the foodservice equipment and supply industry. Our customers are end users such has hotels, restaurants, country clubs, convention centers and casinos as well as distributors of restaurants supplies and equipment, and manufacturers of foodservice equipment and supplies.
Target Market(s)
Hotels, Restaurants, Supply & Equipment Distributors, Foodservice Manufacturers
Industry/Entity Type
Foodservice/Hospitality
Contact Information for Business Card
Name, Title, Contact Number, Email, Website, Social Media, Address
Requirements
Must have
- Clean & Simple but Serious and Impressionable

```html
<!DOCTYPE html>
<html lang="en">
<head>
<meta charset="utf-8">
<title>Harbor Crest Reps – Business Card</title>
<link href="https://fonts.googleapis.com/css2?family=Outfit:wght@400;500;800&display=swap" rel="stylesheet">
<style>
  :root {
    --backdrop: #c3c3c2;
    --card-deep: #1d0f6a;
    --card-bright: #2c1380;
    --gold: #c9a64a;
    --ink-light: #ffffff;
    --ink-soft: #e6e2f4;
  }
  * { box-sizing: border-box; margin: 0; padding: 0; }
  html, body {
    width: 1200px; height: 1000px; overflow: hidden;
    background: var(--backdrop);
    font-family: "Outfit", sans-serif;
  }
  .stage {
    position: relative; width: 1200px; height: 1000px;
  }
  .card {
    position: absolute; left: 320px; width: 560px; height: 320px;
    background: linear-gradient(135deg, var(--card-bright) 0%, var(--card-deep) 100%);
    border-radius: 4px;
    box-shadow: 0 6px 18px rgba(0,0,0,0.18);
    overflow: hidden;
  }
  .card--front { top: 160px; }
  .card--back { top: 520px; }

  .brand-name {
    position: absolute; left: 0; right: 0; top: 140px;
    text-align: center;
    color: var(--gold);
    font-weight: 500; font-size: 30px; letter-spacing: 2px;
  }
  .brand-name--small {
    left: auto; right: 30px; top: 28px;
    font-size: 13px; letter-spacing: 1px; text-align: right;
  }

  .person {
    position: absolute; left: 44px; top: 84px;
  }
  .person__name {
    color: var(--ink-light); font-weight: 800; font-size: 31px; letter-spacing: 0.5px;
    line-height: 1;
  }
  .person__title {
    color: var(--ink-soft); font-weight: 400; font-size: 15px; margin-top: 6px;
  }

  .contact-list {
    position: absolute; left: 44px; top: 170px;
    list-style: none;
  }
  .contact-list li {
    display: flex; align-items: center; gap: 10px;
    height: 27px;
    color: var(--ink-light); font-size: 14px; font-weight: 400;
  }
  .contact-list svg { width: 15px; height: 15px; flex: none; fill: var(--ink-light); }
</style>
</head>
<body>
<main class="stage">
  <section class="card card--front" aria-label="Card front">
    <div class="brand-name">HARBOR CREST REPS</div>
  </section>

  <section class="card card--back" aria-label="Card back">
    <div class="brand-name brand-name--small">HARBOR CREST</div>
    <div class="person">
      <div class="person__name">EVAN MARLOW</div>
      <div class="person__title">Chief Executive Officer</div>
    </div>
    <ul class="contact-list">
      <li>
        <svg viewBox="0 0 24 24" aria-hidden="true"><path d="M6.6 10.8a15 15 0 0 0 6.6 6.6l2.2-2.2a1 1 0 0 1 1-.25 11.4 11.4 0 0 0 3.6.57 1 1 0 0 1 1 1V20a1 1 0 0 1-1 1A17 17 0 0 1 3 4a1 1 0 0 1 1-1h3.5a1 1 0 0 1 1 1c0 1.25.2 2.45.57 3.6a1 1 0 0 1-.25 1z"/></svg>
        (512) 000-0000
      </li>
      <li>
        <svg viewBox="0 0 24 24" aria-hidden="true"><path d="M3 5h18a1 1 0 0 1 1 1v12a1 1 0 0 1-1 1H3a1 1 0 0 1-1-1V6a1 1 0 0 1 1-1zm1 2.3V17h16V7.3l-8 5.2zM5.6 7 12 11.1 18.4 7z"/></svg>
        service@harborcrestreps.com
      </li>
      <li>
        <svg viewBox="0 0 24 24" aria-hidden="true"><circle cx="12" cy="12" r="10"/></svg>
        harborcrestreps
      </li>
      <li>
        <svg viewBox="0 0 24 24" aria-hidden="true"><path d="M12 2a10 10 0 1 0 0 20 10 10 0 0 0 0-20zm6.9 9h-3a15 15 0 0 0-1.4-6A8 8 0 0 1 18.9 11zM12 4c.9 1.3 1.7 3.8 1.9 7h-3.8c.2-3.2 1-5.7 1.9-7zM9.5 5a15 15 0 0 0-1.4 6h-3A8 8 0 0 1 9.5 5zM5.1 13h3a15 15 0 0 0 1.4 6A8 8 0 0 1 5.1 13zM12 20c-.9-1.3-1.7-3.8-1.9-7h3.8c-.2 3.2-1 5.7-1.9 7zm2.5-1a15 15 0 0 0 1.4-6h3a8 8 0 0 1-4.4 6z"/></svg>
        www.harborcrestreps.com
      </li>
      <li>
        <svg viewBox="0 0 24 24" aria-hidden="true"><path d="M12 2a7 7 0 0 0-7 7c0 5 7 13 7 13s7-8 7-13a7 7 0 0 0-7-7zm0 9.5A2.5 2.5 0 1 1 12 6.5a2.5 2.5 0 0 1 0 5z"/></svg>
        0000 Texas Blvd · Austin, TX 00000-0000
      </li>
    </ul>
  </section>
</main>
</body>
</html>
```